Copperfield Wire - Subscription Landing page

we need responsive landing page for a new news service about the Blockchain innovations coins and startups, the landing page includes vertical video player and call to action button, attach mockup.
temporary page
http://www.cpfw.io/
1 page

```html
<!DOCTYPE html>
<html lang="en">
<head>
<meta charset="utf-8">
<title>Copperfield Wire – Subscribe</title>
<link rel="stylesheet" href="https://fonts.googleapis.com/css2?family=Poppins:wght@400;500;600;700&display=swap">
<style>
  :root {
    --brand-red: #e8202a;
    --header-bg: #ffffff;
    --tagline: #4a4a4a;
    --hero-deep: #05080d;
    --hero-mid: #0d1a2a;
    --hero-glow: #1d3550;
    --text-light: #ffffff;
    --footer-text: #e6e6e6;
    --device-frame: #2a2c31;
    --device-edge: #4a4d55;
    --screen-top: #3c4a66;
    --screen-mid: #c9a7a4;
    --screen-low: #eadbd6;
    --play-bg: rgba(30, 30, 30, 0.82);
  }
  * { box-sizing: border-box; margin: 0; padding: 0; }
  html, body { width: 1200px; height: 686px; overflow: hidden; }
  body { font-family: "Poppins", sans-serif; background: var(--hero-deep); }

  .page { position: relative; width: 1200px; height: 686px; overflow: hidden; }

  .site-header {
    position: absolute; left: 0; top: 0; width: 1200px; height: 103px;
    background: var(--header-bg);
  }
  .brand {
    position: absolute; left: 117px; top: 31px;
    display: flex; align-items: center; gap: 12px;
  }
  .brand-mark {
    width: 40px; height: 40px; border-radius: 8px; background: var(--brand-red);
  }
  .brand-name {
    font-size: 27px; font-weight: 600; color: var(--brand-red); letter-spacing: -0.3px;
  }
  .tagline {
    position: absolute; left: 596px; top: 33px;
    font-size: 27.5px; font-weight: 500; color: var(--tagline); letter-spacing: -0.2px;
  }

  .hero {
    position: absolute; left: 0; top: 103px; width: 1200px; height: 583px;
    background:
      radial-gradient(ellipse 520px 300px at 820px 280px, var(--hero-glow) 0%, rgba(29,53,80,0) 70%),
      radial-gradient(ellipse 500px 260px at 300px 420px, #1a2c40 0%, rgba(26,44,64,0) 70%),
      linear-gradient(180deg, var(--hero-deep) 0%, var(--hero-mid) 100%);
  }

  .video-device {
    position: absolute; left: 197px; top: 210px; width: 194px; height: 386px;
    border-radius: 30px; background: var(--device-frame);
    border: 2px solid var(--device-edge);
    box-shadow: 0 18px 40px rgba(0,0,0,0.55);
  }
  .video-screen {
    position: absolute; left: 10px; top: 10px; right: 10px; bottom: 10px;
    border-radius: 22px; overflow: hidden;
    background: linear-gradient(180deg, var(--screen-top) 0%, var(--screen-mid) 45%, var(--screen-low) 100%);
  }
  .video-bar {
    position: absolute; left: 0; top: 0; width: 100%; height: 26px;
    background: rgba(0,0,0,0.35);
  }
  .play-button {
    position: absolute; left: 50%; top: 50%; width: 50px; height: 34px;
    margin: -17px 0 0 -25px; border-radius: 8px; background: var(--play-bg);
    display: flex; align-items: center; justify-content: center;
  }

  .intro {
    position: absolute; left: 510px; top: 226px; width: 500px;
    font-size: 22px; line-height: 34px; font-weight: 400; color: var(--text-light);
  }
  .subscribe-title {
    position: absolute; left: 510px; top: 352px; width: 470px;
    font-size: 27.5px; line-height: 38px; font-weight: 600; color: var(--text-light);
  }
  .cta {
    position: absolute; left: 512px; top: 452px; width: 341px; height: 63px;
    border: 2px solid var(--text-light); border-radius: 32px;
    display: flex; align-items: center; justify-content: center;
    font-size: 20.5px; font-weight: 600; color: var(--text-light);
  }
  .social-links {
    position: absolute; left: 520px; top: 546px; display: flex; gap: 16px;
  }
  .social-links span {
    width: 18px; height: 18px; border-radius: 50%; background: var(--text-light);
  }

  .site-footer {
    position: absolute; left: 0; top: 636px; width: 1200px; text-align: center;
    font-size: 14px; color: var(--footer-text);
  }
</style>
</head>
<body>
<div class="page">
  <header class="site-header">
    <div class="brand">
      <span class="brand-mark"></span>
      <span class="brand-name">Copperfield Wire</span>
    </div>
    <div class="tagline">BE READY FOR TOMORROW</div>
  </header>

  <section class="hero" role="img" aria-label="Dark blue background of glowing network lines and soft city lights"></section>

  <div class="video-device">
    <div class="video-screen" role="img" aria-label="Vertical video player showing the daily news story with a presenter in front of a city skyline">
      <div class="video-bar"></div>
      <div class="play-button">
        <svg width="14" height="16" viewBox="0 0 14 16" aria-hidden="true"><path d="M1 1 L13 8 L1 15 Z" fill="#ffffff"/></svg>
      </div>
    </div>
  </div>

  <p class="intro">Stay updated with all the latest blockchain innovations coins and startups in a daily video story.</p>
  <h2 class="subscribe-title">Subscribe for free in one of our channels below:</h2>
  <div class="cta">Browser Notification</div>
  <nav class="social-links" aria-label="Social channels">
    <span></span><span></span><span></span><span></span>
  </nav>

  <footer class="site-footer">Copyrights © 2018 | All Rights Reserved&nbsp; | &nbsp;Privacy policy&nbsp; | &nbsp;Terms and conditions</footer>
</div>
</body>
</html>
```